KM Group

We need a new website for our company and since we had a very good work done for our logo in this site, we're back for the entire job.

Our company name is Halvorsen Capital Group. We're adding files of examples of what we have done today. In my opinion we need a more attention lock in the site but yet financial simple work.

Our files (attached) will let you know what we have so far. We need a complete change but the colours should be the same, however you can change them not running away to far from the original, and of course matching with the logo.

We need examples for 3 kind of layouts.

- A HOME welcome layout
- An internal Layout with sidebar
- And internal Layout wide

We can buy image licenses if needed for assets.
Actually there are 5 slide images placed on the Welcome HOME, we need those there, but you can improve with better images to match the new website!!!

Target Market(s)

Clients looking for financial advisers, tax and funds specialist, currency advisers

Industry/Entity Type

Financial

Requirements
Must have
• all the fonts must be in accordance with the financial market sites........the welcome home page must be precise, neat and information accurate........the menu should be elegant........main focus on the Home page, should be also the PRIVATE ACCESS box log in.......

```html
<!DOCTYPE html>
<html lang="en">
<head>
<meta charset="utf-8">
<title>Halvorsen Capital Group</title>
<link rel="stylesheet" href="https://fonts.googleapis.com/css2?family=Oswald:wght@300;400&family=Arimo:wght@400;700&display=swap">
<style>
:root{
  --orange:#f47b20;
  --orange-soft:rgba(244,123,32,.85);
  --ink:#222;
  --dark:#2b2b2b;
  --page:#f4f4f4;
  --white:#fff;
  --line:#f3a66b;
  --up:#0a8a5a;
  --down:#e01b1b;
}
*{margin:0;padding:0;box-sizing:border-box}
html,body{width:1130px;height:1200px;overflow:hidden}
body{position:relative;background:var(--page);font-family:"Arimo",Arial,sans-serif;color:var(--ink)}
.abs{position:absolute}
.hero-backdrop{left:0;top:0;width:1130px;height:432px;background:linear-gradient(100deg,#3c4a5c 0%,#7f8fa3 30%,#b9c4cf 55%,#8797aa 80%,#56667a 100%)}
.topbar{left:235px;top:0;width:659px;height:35px;background:var(--orange);display:flex;justify-content:flex-end;align-items:center;gap:16px;padding-right:13px}
.topbar a{font-family:"Oswald",sans-serif;font-weight:300;color:var(--white);font-size:14px;text-decoration:none;display:flex;align-items:center;gap:6px;white-space:nowrap}
.header{left:235px;top:35px;width:659px;height:74px;background:var(--white)}
.brand{left:8px;top:0;width:148px;height:74px;display:flex;align-items:center;gap:5px;padding-top:20px;font-family:"Oswald",sans-serif;font-weight:400;font-size:11px;color:var(--dark);letter-spacing:.2px;white-space:nowrap}
.brand .mark{width:10px;height:10px;background:var(--orange);flex:none}
.nav{left:159px;top:0;width:433px;height:74px;display:flex;justify-content:space-between}
.nav a{font-family:"Oswald",sans-serif;font-weight:400;font-size:12px;color:var(--ink);text-decoration:none;line-height:74px;white-space:nowrap}
.nav a.active{background:var(--orange);color:var(--white);width:44px;text-align:center}
.search{left:603px;top:0;width:56px;height:64px;background:var(--orange);border-bottom-left-radius:56px}
.slider{left:235px;top:122px;width:659px;height:212px;background:linear-gradient(90deg,#c9b8a6 0%,#ddd4c8 40%,#6d7f9b 70%,#42577a 100%)}
.slide-title{left:19px;top:104px;background:var(--white);padding:0 10px;height:37px;line-height:37px;font-family:"Oswald",sans-serif;font-size:20.5px;color:var(--orange);white-space:nowrap}
.slide-text{left:19px;top:140px;width:282px;height:34px;background:var(--orange-soft);color:var(--white);font-size:9px;line-height:11px;padding:6px 13px;white-space:nowrap}
.btn{display:inline-block;background:var(--dark);color:var(--white);font-family:"Oswald",sans-serif;font-size:10.5px;padding:0 8px;height:19px;line-height:19px;white-space:nowrap}
.slide-btn{left:19px;top:175px}
.welcome{left:235px;top:347px;width:431px;height:146px;background:var(--white);border:1px solid #cfcfcf;padding:10px 12px}
.welcome h1{font-family:"Oswald",sans-serif;font-weight:300;font-size:21px;color:var(--ink);margin-bottom:10px;white-space:nowrap}
.welcome h1 span{color:var(--orange);font-weight:400}
.body-text{font-size:8.3px;line-height:13.1px;color:var(--ink)}
.access{left:690px;top:347px;width:204px;height:146px;background:var(--orange);padding:9px 10px}
.access h2{font-family:"Oswald",sans-serif;font-weight:400;font-size:21px;color:var(--white);text-align:center;margin-bottom:6px}
.access .field{height:21px;background:var(--white);border:1px solid #f8c49b;margin-bottom:6px}
.access .forgot{font-size:8px;color:#fde3cf;margin:3px 0 6px}
.card{top:512px;width:204px}
.card .photo{height:146px;position:relative}
.card .label{position:absolute;left:0;bottom:0;width:100%;height:36px;background:var(--orange-soft);color:var(--white);font-family:"Oswald",sans-serif;font-size:15px;line-height:36px;padding-left:13px;white-space:nowrap}
.card .body-text{margin-top:8px;height:73px}
.ticker{left:235px;top:779px;width:659px;height:24px;border:1px solid #cfcfcf;background:#f7f7f5;display:flex;justify-content:center;align-items:center;gap:12px;font-size:8.3px;white-space:nowrap}
.ticker .up{color:var(--up)}
.ticker .down{color:var(--down)}
.footer{left:0;top:832px;width:1130px;height:314px;background:var(--white)}
.verified{left:235px;top:24px;font-family:"Oswald",sans-serif;font-weight:300;font-size:19px;color:var(--ink);white-space:nowrap}
.badge{top:18px;height:32px;background:#d9dde3}
.rule{left:235px;width:659px;height:1px;background:var(--line)}
.col h3{font-family:"Oswald",sans-serif;font-weight:400;font-size:18px;color:var(--ink);margin-bottom:8px;white-space:nowrap}
.col li{list-style:none;font-size:8.3px;line-height:13.1px;white-space:nowrap}
.legal{left:235px;top:260px;width:659px;font-size:8.3px;line-height:13.1px}
.bottombar{left:0;top:1146px;width:1130px;height:54px;background:var(--dark);color:#ddd;font-size:8.5px}
</style>
</head>
<body>
<div class="abs hero-backdrop" role="img" aria-label="Blurred photo of financial charts with a dotted world map"></div>

<div class="abs topbar">
  <a href="#"><svg width="14" height="14" viewBox="0 0 14 14"><rect x="1" y="2" width="10" height="11" fill="none" stroke="#fff" stroke-width="1.3"/><path d="M5 9 L12 2" stroke="#fff" stroke-width="1.5"/></svg>APPLE NOW</a>
  <a href="#"><svg width="16" height="13" viewBox="0 0 16 13"><path d="M1 5 L8 1 L15 5 V12 H1 Z" fill="none" stroke="#fff" stroke-width="1.3"/><path d="M1 5 L8 9 L15 5" fill="none" stroke="#fff" stroke-width="1.3"/></svg>CONTACT US</a>
</div>

<div class="abs header">
  <div class="abs brand"><span class="mark"></span>HALVORSEN CAPITAL GROUP</div>
  <nav class="abs nav">
    <a class="active" href="#">HOME</a><a href="#">ABOUT US</a><a href="#">INVESTMENTS</a><a href="#">FUNDS</a><a href="#">BROKERAGE</a><a href="#">EXCHANGE</a><a href="#">ACCOUNTS</a>
  </nav>
  <div class="abs search"><svg class="abs" style="left:18px;top:14px" width="28" height="28" viewBox="0 0 28 28"><circle cx="17" cy="11" r="8" fill="none" stroke="#fff" stroke-width="3"/><path d="M11 17 L3 25" stroke="#fff" stroke-width="4" stroke-linecap="round"/></svg></div>
</div>

<div class="abs slider" role="img" aria-label="Photo of two smiling businessmen in a bright modern office with a glass roof">
  <div class="abs slide-title">FIND YOUR OWN SOLUTION</div>
  <div class="abs slide-text">Find the way of saving and investing that Suits you Best.<br>We will help you understand your situation and your potential.</div>
  <span class="abs btn slide-btn">READ MORE</span>
</div>

<section class="abs welcome">
  <h1><span>WELCOME TO</span> HALVORSEN CAPITAL GROUP.</h1>
  <p class="body-text"><b>Lorem Ipsum</b> is simply dummy text of the printing and typesetting industry. Lorem Ipsum has been the industry's standard dummy text ever since the 1500s, when an unknown printer took a galley of type and scrambled it to make a type specimen book. It has survived not only five centuries, but also the leap into electronic typesetting, remaining essentially unchanged. It was popularised in the 1960s with the release of Letraset sheets containing Lorem Ipsum passages, and more recently with desktop publishing software like Aldus PageMaker including versions of Lorem Ipsum.</p>
</section>

<section class="abs access">
  <h2>PRIVATE ACCESS</h2>
  <div class="field"></div>
  <div class="field"></div>
  <p class="forgot">Forget acc number / password?</p>
  <span class="btn">LOG IN TO ACCOUNTS</span>
</section>

<article class="abs card" style="left:235px">
  <div class="photo" role="img" aria-label="Photo of bronze gears with currency symbols" style="background:linear-gradient(135deg,#8a5a3a,#d9a578 50%,#6b4028)"><div class="label">MANAGMFFENT &amp; STRATEGY</div></div>
  <p class="body-text"><b>Lorem Ipsum</b> is simply dummy text of the printing and typesetting industry. Lorem Ipsum has been the industry's standard dummy text ever since the 1500s, when an unknown printer took a galley of type and scrambled it to make a type specimen book.</p>
  <span class="btn">READ MORE</span>
</article>
<article class="abs card" style="left:463px">
  <div class="photo" role="img" aria-label="Photo of a businesswoman sitting at a desk in an office" style="background:linear-gradient(135deg,#e6e3de,#b8a894 50%,#8b7a68)"><div class="label">FUNDS</div></div>
  <p class="body-text"><b>Lorem Ipsum</b> is simply dummy text of the printing and typesetting industry. Lorem Ipsum has been the industry's standard dummy text ever since the 1500s, when an unknown printer took a galley of type and scrambled it to make a type specimen book.</p>
  <span class="btn">READ MORE</span>
</article>
<article class="abs card" style="left:690px">
  <div class="photo" role="img" aria-label="Photo of currency charts under a magnifying glass" style="background:linear-gradient(135deg,#e9e9e4,#c9ccc8 50%,#a9aea9)"><div class="label">CURRENCY FEXCHANGE</div></div>
  <p class="body-text"><b>Lorem Ipsum</b> is simply dummy text of the printing and typesetting industry. Lorem Ipsum has been the industry's standard dummy text ever since the 1500s, when an unknown printer took a galley of type and scrambled it to make a type specimen book.</p>
  <span class="btn">READ MORE</span>
</article>

<div class="abs ticker">
  <span>GBP/EUR = <span class="up">1.18833 ▲</span></span>
  <span>GBP/AUD = <span class="up">1.70716 ▲</span></span>
  <span>GBP/CAD = <span class="down">1.63763 ▼</span></span>
  <span>GBP/USD = <span class="down">1.5586 ▼</span></span>
  <span>GBP/NZD = <span class="down">1.97482 ▼</span></span>
  <span>GBP/TRY = <span class="up">3.22321 ▲</span></span>
</div>

<footer class="abs footer">
  <div class="abs verified">VERIFIED AND PROTECTED BY</div>
  <div class="abs badge" style="left:518px;width:85px"></div>
  <div class="abs badge" style="left:627px;width:34px;border-radius:50%;top:16px;height:34px"></div>
  <div class="abs badge" style="left:688px;width:74px"></div>
  <div class="abs badge" style="left:790px;width:105px"></div>
  <div class="abs rule" style="top:64px"></div>

  <div class="abs col" style="left:235px;top:80px"><h3>ABOUT</h3><ul><li>History</li><li>Expertiza</li><li>Identity</li><li>Strategy</li><li>Contact us</li></ul></div>
  <div class="abs col" style="left:340px;top:80px"><h3>INVEFSTMENTS</h3><ul><li>Term Defposits</li><li>Managment &amp; Strategy</li><li>Client Relations</li><li>Financial Privacy</li><li>Tax Advice</li><li>Wealth Analysis &amp; Financial Planning</li><li>Active Advisory Group</li><li>Manager Selection Services</li><li>Private Equity</li></ul></div>
  <div class="abs col" style="left:518px;top:80px"><h3>FUNDS</h3><ul><li>Overview</li><li>Administration</li><li>Funds Security</li><li>Core Services</li><li>Reporting</li><li>Revenue oportunities</li><li>How it works?</li><li>Glossary</li></ul></div>
  <div class="abs col" style="left:641px;top:80px"><h3>CURRENCY EXCHANGE</h3><ul><li>Foreign Exchange</li><li>Fx Forward</li><li>Fx Options</li></ul></div>
  <div class="abs col" style="left:641px;top:159px"><h3>ACCOUNTS</h3><ul><li>Appply Now</li><li>Private Access</li></ul></div>
  <div class="abs col" style="left:816px;top:80px"><h3>BROKERAGE</h3><ul><li>Institutional</li><li>Research</li><li>Trading</li></ul></div>

  <div class="abs rule" style="top:243px"></div>
  <p class="abs legal">Lorem Ipsum has been the industry's standard dummy text ever since the 1500s, when an unknown printer took a galley of type and scrambled it to make a type specimen book. It has survived not only five centuries, but also the leap into electronic typesetting, remaining essentially unchanged. It was popularised in the 1960s with the release of Letraset sheets containing Lorem Ipsum passages, and more recently with desktop publishing software like Aldus PageMaker including versions of Lorem Ipsum.</p>
</footer>

<div class="abs bottombar"><span class="abs" style="left:235px;top:23px">© Halvorsen Capital 2013</span></div>
</body>
</html>
```